The Perfect Business Card for PineHarbor

I am looking for a business card which beautifully incorporates my logo, reflects my business and looks special, elegant and clean.

```html
<!DOCTYPE html>
<html lang="en">
<head>
<meta charset="utf-8">
<title>PineHarbor Business Card</title>
<link rel="stylesheet" href="https://fonts.googleapis.com/css2?family=Cormorant+Garamond:wght@500;600&display=swap">
<style>
  :root {
    --backdrop: #dfe1e1;
    --card: #000000;
    --accent: #7b9a3c;
    --shadow: rgba(0, 0, 0, 0.25);
  }
  * { margin: 0; padding: 0; box-sizing: border-box; }
  html, body {
    width: 1200px;
    height: 875px;
    overflow: hidden;
    background: var(--backdrop);
    font-family: "Cormorant Garamond", Georgia, serif;
    color: var(--accent);
  }
  .stage {
    position: relative;
    width: 1200px;
    height: 875px;
  }
  .card {
    position: absolute;
    top: 283px;
    width: 540px;
    height: 309px;
    background: var(--card);
    box-shadow: 0 18px 40px var(--shadow);
  }
  .card--front { left: 40px; }
  .card--back { left: 620px; }

  .brand {
    position: absolute;
    display: flex;
    align-items: center;
    gap: 12px;
  }
  .brand__dot {
    width: 34px;
    height: 34px;
    border: 2px solid var(--accent);
    border-radius: 50%;
  }
  .brand__name {
    font-weight: 600;
    font-size: 40px;
    letter-spacing: 1px;
    color: var(--accent);
  }
  .card--front .brand {
    left: 50%;
    top: 50%;
    transform: translate(-50%, -50%);
  }
  .card--back .brand {
    left: 28px;
    top: 128px;
  }
  .card--back .brand__name { font-size: 32px; }
  .card--back .brand__dot { width: 28px; height: 28px; }

  .divider {
    position: absolute;
    left: 262px;
    width: 1.5px;
    background: var(--accent);
  }
  .divider--top { top: 0; height: 58px; }
  .divider--bottom { bottom: 0; height: 48px; }

  .identity {
    position: absolute;
    left: 300px;
    top: 22px;
  }
  .identity__name {
    font-weight: 500;
    font-size: 30px;
    letter-spacing: 1px;
    line-height: 1;
  }
  .identity__role {
    font-weight: 500;
    font-size: 15px;
    letter-spacing: 1px;
    margin-top: 4px;
  }

  .contact-list {
    position: absolute;
    left: 252px;
    top: 96px;
    list-style: none;
  }
  .contact-list__item {
    display: flex;
    align-items: center;
    height: 38px;
    font-weight: 500;
    font-size: 16px;
    letter-spacing: 1px;
  }
  .contact-list__icon {
    width: 20px;
    height: 20px;
    margin-right: 28px;
    fill: var(--accent);
  }
</style>
</head>
<body>
<main class="stage">
  <section class="card card--front" aria-label="Card front">
    <div class="brand">
      <span class="brand__dot"></span>
      <span class="brand__name">PineHarbor</span>
    </div>
  </section>

  <section class="card card--back" aria-label="Card back">
    <div class="brand">
      <span class="brand__dot"></span>
      <span class="brand__name">PineHarbor</span>
    </div>

    <span class="divider divider--top"></span>
    <span class="divider divider--bottom"></span>

    <div class="identity">
      <p class="identity__name">XXXXX XXX</p>
      <p class="identity__role">XXXXX XXXXX</p>
    </div>

    <ul class="contact-list">
      <li class="contact-list__item">
        <svg class="contact-list__icon" viewBox="0 0 24 24" aria-label="Phone"><path d="M6.6 10.8a15 15 0 0 0 6.6 6.6l2.2-2.2c.3-.3.7-.4 1-.2 1.1.4 2.3.6 3.6.6.6 0 1 .4 1 1V20c0 .6-.4 1-1 1A17 17 0 0 1 3 4c0-.6.4-1 1-1h3.5c.6 0 1 .4 1 1 0 1.3.2 2.5.6 3.6.1.3 0 .7-.2 1z"/></svg>
        <span>XXXXX XXXXX XX</span>
      </li>
      <li class="contact-list__item">
        <svg class="contact-list__icon" viewBox="0 0 24 24" aria-label="Location"><path d="M12 2a7 7 0 0 0-7 7c0 5.2 7 13 7 13s7-7.8 7-13a7 7 0 0 0-7-7zm0 9.5A2.5 2.5 0 1 1 12 6.5a2.5 2.5 0 0 1 0 5z"/></svg>
        <span>XXXXX XXXXXX XXXXXX</span>
      </li>
      <li class="contact-list__item">
        <svg class="contact-list__icon" viewBox="0 0 24 24" aria-label="Website"><circle cx="12" cy="12" r="9" fill="none" stroke="currentColor" stroke-width="2" style="stroke:var(--accent)"/><path d="M3 12h18M12 3c3 3 3 15 0 18M12 3c-3 3-3 15 0 18" fill="none" style="stroke:var(--accent)" stroke-width="1.6"/></svg>
        <span>XXXXX XXXX XXXXX</span>
      </li>
      <li class="contact-list__item">
        <svg class="contact-list__icon" viewBox="0 0 24 24" aria-label="Email"><path d="M3 5h18v14H3z M3 5l9 7 9-7" fill="none" style="stroke:var(--accent)" stroke-width="2"/></svg>
        <span>XXXXX XXXXXXXXXX</span>
      </li>
    </ul>
  </section>
</main>
</body>
</html>
```